Crestline Lawn and Stoneworks Flyer/Brochure

Flyer/Brochure for artificial turf and paver company. Photos and txt<br/>Specializes in Turf, Pavers, Patio, Decorative Rock, Hardscape, Landscape Design.

Target Market(s)

Homeowners

Industry/Entity Type

Construction

Font styles to use
Sans Serif

Colors
9bcb3c

Requirements
Must have
• Photos, we will provide as well as logo
• phone number and email address
• similar branding as website
• www.crestlinelsw.com
Nice to have
• eye catching not too busy
• clean and easy to read
• Hi! Please see photos on our instagram - there are a couple shots that may be better than the website there.
• Also, photo of dog on turf. Please mention kid -play turf and pet turf is available or something like "your pup will love our pet turf"
• Add- "Ask us about our specials"
• phone number is 800-417-3286

```html
<!DOCTYPE html>
<html lang="en">
<head>
<meta charset="utf-8">
<title>Crestline Lawn and Stoneworks – Outdoor Living Flyer</title>
<link href="https://fonts.googleapis.com/css2?family=Anton&family=Montserrat:wght@700&family=Dosis:wght@400;600&display=swap" rel="stylesheet">
<style>
  :root{
    --green:#6cbe45;
    --green-bright:#7dc242;
    --dark:#2e2e30;
    --dark-soft:#3a3a3d;
    --white:#ffffff;
    --ink:#0c0c0c;
  }
  *{margin:0;padding:0;box-sizing:border-box}
  html,body{width:848px;height:1200px;overflow:hidden;background:var(--dark)}
  .flyer{position:relative;width:848px;height:1200px;overflow:hidden;background:var(--dark)}
  .backdrop{position:absolute;inset:0}
  .brand{position:absolute;top:46px;left:0;width:100%;text-align:center;
    font-family:'Montserrat',sans-serif;font-weight:700;color:var(--white);
    font-size:34px;line-height:1.2;letter-spacing:1px}
  .headline{position:absolute;top:248px;left:0;width:100%;text-align:center;
    font-family:'Anton',sans-serif;color:var(--ink);line-height:1}
  .headline .lead{display:block;font-size:52px}
  .headline .main{display:block;font-size:68px;margin-top:-2px}
  .headline .tail{display:block;font-size:36px;letter-spacing:17px;margin-top:2px;padding-left:17px}
  .specialties{position:absolute;top:704px;left:0;width:100%;text-align:center;
    font-family:'Anton',sans-serif;line-height:1}
  .specialties .title{display:block;font-size:58px;color:var(--green-bright)}
  .specialties .subtitle{display:block;font-size:38px;color:var(--white);margin-top:6px}
  .services{position:absolute;top:834px;left:0;width:100%;height:120px}
  .service{position:absolute;width:140px;margin-left:-70px;text-align:center;
    font-family:'Dosis',sans-serif;font-weight:400;font-size:23px;color:var(--white)}
  .service svg{display:block;margin:0 auto 12px;width:72px;height:72px;
    fill:none;stroke:var(--green-bright);stroke-width:4;stroke-linejoin:round;stroke-linecap:round}
  .service svg .solid{fill:var(--green-bright);stroke:none}
  .contact{position:absolute;top:1076px;left:0;width:100%;text-align:center;
    font-family:'Dosis',sans-serif;color:var(--white)}
  .contact .phone{display:block;font-size:30px;font-weight:600;letter-spacing:1px}
  .contact .line{display:block;font-size:17px;margin-top:2px;letter-spacing:.3px}
</style>
</head>
<body>
<main class="flyer">
  <svg class="backdrop" width="848" height="1200" viewBox="0 0 848 1200">
    <defs>
      <linearGradient id="skyTone" x1="0" y1="0" x2="0" y2="1">
        <stop offset="0" stop-color="#6b6a2a"/>
        <stop offset=".45" stop-color="#a9a55a"/>
        <stop offset=".78" stop-color="#8fa866"/>
        <stop offset=".82" stop-color="#5f8d2c"/>
        <stop offset="1" stop-color="#3f6b1c"/>
      </linearGradient>
      <linearGradient id="skyTint" x1="0" y1="0" x2="1" y2="0">
        <stop offset="0" stop-color="#c9b94a" stop-opacity=".25"/>
        <stop offset="1" stop-color="#4f8a7a" stop-opacity=".45"/>
      </linearGradient>
    </defs>
    <path class="photo-edge" fill="#ffffff" d="M0 0H848V505C700 615 500 690 250 670C150 660 60 600 0 560Z"/>
    <g role="img" aria-label="Photo: a person walking down a row of a green crop field under a stormy golden sky">
      <path fill="url(#skyTone)" d="M0 0H848V505C700 600 500 668 260 656C150 646 60 590 0 550Z"/>
      <path fill="url(#skyTint)" d="M0 0H848V505C700 600 500 668 260 656C150 646 60 590 0 550Z"/>
    </g>
    <path class="contact-edge" fill="#ffffff" d="M0 1152C200 1030 420 1005 520 1012C640 1022 760 1045 848 1068V1200H0Z"/>
    <path class="contact-band" fill="var(--green)" d="M0 1170C200 1045 420 1020 520 1027C640 1037 760 1060 848 1082V1200H0Z"/>
  </svg>

  <div class="brand">CRESTLINE<br>LAWN AND STONEWORKS</div>

  <h1 class="headline">
    <span class="lead">MAKE YOUR</span>
    <span class="main">OUTDOOR LIVING</span>
    <span class="tail">VISION A REALITY</span>
  </h1>

  <h2 class="specialties">
    <span class="title">SPECIALIZES</span>
    <span class="subtitle">FOR OUR OUTDOOR LIVING</span>
  </h2>

  <section class="services">
    <div class="service" style="left:78px">
      <svg viewBox="0 0 72 72"><path class="solid" d="M4 68C6 50 4 38 0 28C10 36 14 48 15 58C16 42 20 28 30 16C26 32 27 46 30 60C32 44 38 32 48 24C44 38 44 50 46 62C50 50 58 42 70 38C62 48 60 58 62 68Z"/></svg>
      Turf
    </div>
    <div class="service" style="left:210px">
      <svg viewBox="0 0 100 72" style="width:100px"><rect x="22" y="8" width="44" height="6"/><path d="M28 14V36M60 14V36"/><rect x="16" y="36" width="56" height="14"/><circle cx="26" cy="56" r="10"/><circle cx="68" cy="56" r="12"/><path d="M2 68H98M80 44L92 40"/></svg>
      Pavers
    </div>
    <div class="service" style="left:343px">
      <svg viewBox="0 0 72 72"><path d="M6 26C14 10 58 10 66 26ZM6 26V32M66 26V32M36 6V70M16 70L22 56H32M56 70L50 56H40M14 56H58"/></svg>
      Patio
    </div>
    <div class="service" style="left:480px">
      <svg viewBox="0 0 72 72"><ellipse cx="38" cy="10" rx="10" ry="6"/><ellipse cx="38" cy="24" rx="16" ry="7"/><ellipse cx="38" cy="40" rx="20" ry="8"/><path d="M4 66C14 56 26 54 38 58C50 54 60 58 68 66Z"/><circle cx="60" cy="54" r="5"/><circle cx="20" cy="58" r="4"/></svg>
      Rock
    </div>
    <div class="service" style="left:611px">
      <svg viewBox="0 0 72 72"><rect x="4" y="4" width="64" height="64" rx="4"/><path d="M4 24H22L30 4M22 24L26 44H4M26 44L44 40L50 68M44 40L52 20L68 24M52 20L42 4M26 44L30 68"/></svg>
      Hardscape
    </div>
    <div class="service" style="left:746px">
      <svg viewBox="0 0 80 72" style="width:80px"><path d="M4 40C24 30 50 30 76 38M4 54C24 44 50 46 76 56M20 70C32 56 48 50 70 48M24 30V18L34 10L44 18V30M30 30V22H38V30"/><path d="M62 30V14M62 24C52 18 56 6 62 2C68 6 72 18 62 24Z"/></svg>
      Landscape
    </div>
  </section>

  <address class="contact">
    <span class="phone">+1 800 417 3286</span>
    <span class="line">info@crestlinelsw.com &nbsp;|&nbsp; www.crestlinelsw.com</span>
    <span class="line">2250 Meadowbrook Ave, Fairview, CA 92801, USA</span>
  </address>
</main>
</body>
</html>
```